TovarTunes poster

We need a poster to promote my live music show for hotels, Im playing for tourists in hotels in Palma de Mallorca, Spain, I would like to see the url of my web site in the poster www.tovartunes.es, in the web site you can see some of my music, thx

```html
<!DOCTYPE html>
<html lang="en">
<head>
<meta charset="utf-8">
<title>TovarTunes – Live Poster</title>
<link href="https://fonts.googleapis.com/css2?family=Great+Vibes&family=Arimo:wght@400;700&display=swap" rel="stylesheet">
<style>
  :root{
    --backdrop:#e9e7e3;
    --sky-teal:#08c6da;
    --deep-night:#0f1e1d;
    --brand-orange:#f07a1a;
    --paper-white:#ffffff;
    --soft-white:#e8f0ef;
  }
  html,body{margin:0;padding:0;width:1200px;height:848px;overflow:hidden;background:var(--backdrop);}
  .poster{
    position:absolute;left:318px;top:24px;width:564px;height:800px;
    background:var(--sky-teal);overflow:hidden;font-family:"Arimo",Arial,sans-serif;
    box-shadow:0 2px 10px rgba(0,0,0,.15);
  }
  .title-row{position:absolute;left:0;top:40px;width:100%;height:110px;}
  .title-swash{position:absolute;left:0;top:0;width:100%;height:110px;}
  .title{
    position:absolute;left:0;top:4px;width:100%;text-align:center;margin:0;
    font-family:"Great Vibes",cursive;font-weight:400;font-size:92px;line-height:1;
    color:var(--paper-white);
  }
  .stage-photo{
    position:absolute;left:0;top:150px;width:100%;height:460px;
    background:linear-gradient(180deg,#2c6b55 0%,#5d8f74 12%,#1fb6c4 24%,#27a9b6 38%,#e9eef0 48%,#c9b7a0 62%,#a89580 80%,#8a7a68 100%);
  }
  .night-band{position:absolute;left:0;top:480px;width:100%;height:320px;}
  .event{position:absolute;color:var(--paper-white);}
  .date{position:absolute;left:170px;width:40px;color:var(--brand-orange);text-align:center;}
  .date .day{display:block;font-size:23px;line-height:1;}
  .date .month{display:block;font-size:14px;line-height:1.2;}
  .venue{position:absolute;left:220px;font-size:9.6px;line-height:1.25;font-weight:700;text-transform:uppercase;color:var(--soft-white);}
  .time{position:absolute;left:220px;font-size:15px;color:var(--soft-white);}
  .time small{font-size:9px;}
  .live{
    position:absolute;left:26px;top:680px;margin:0;
    font-family:"Great Vibes",cursive;font-weight:400;font-size:64px;line-height:1;color:var(--brand-orange);
  }
  .contact{position:absolute;top:758px;font-size:14.5px;color:var(--soft-white);}
  .contact .label{color:var(--brand-orange);margin-right:10px;}
  .brand-mark{
    position:absolute;left:474px;top:742px;display:flex;align-items:center;gap:5px;
    font-family:"Arimo",Arial,sans-serif;font-weight:700;font-size:13px;color:var(--paper-white);
  }
  .brand-mark .dot{width:8px;height:8px;border-radius:50%;background:var(--paper-white);}
</style>
</head>
<body>
  <main class="poster">
    <div class="title-row">
      <svg class="title-swash" viewBox="0 0 564 110" aria-hidden="true">
        <path d="M30 82 Q120 70 190 76" stroke="#ffffff" stroke-width="2" fill="none" stroke-linecap="round"/>
        <path d="M380 76 Q450 70 534 82" stroke="#ffffff" stroke-width="2" fill="none" stroke-linecap="round"/>
      </svg>
      <h1 class="title">tovartunes</h1>
    </div>

    <div class="stage-photo" role="img" aria-label="Guitarist playing seated on a hotel terrace by the harbour at dusk, with a microphone stand and amplifier"></div>

    <svg class="night-band" viewBox="0 0 564 320" preserveAspectRatio="none" aria-hidden="true">
      <path d="M0 122 C120 60 300 40 564 40 L564 320 L0 320 Z" fill="#0f1e1d"/>
      <path d="M0 122 C120 60 300 40 564 40" stroke="#f2f2f0" stroke-width="6" fill="none" opacity=".85"/>
    </svg>

    <div class="date" style="top:636px"><span class="day">14</span><span class="month">JUN</span></div>
    <div class="venue" style="top:638px">Bay Terrace 12 Harbour Lane Street<br>Number 8.14 - Old Town</div>
    <div class="time" style="top:660px">Starts at &nbsp;08.00 <small>PM</small></div>

    <div class="date" style="top:702px"><span class="day">14</span><span class="month">JUN</span></div>
    <div class="venue" style="top:704px">Bay Terrace 12 Harbour Lane Street<br>Number 8.14 - Old Town</div>
    <div class="time" style="top:726px">Starts at &nbsp;08.00 <small>PM</small></div>

    <p class="live">Live</p>

    <div class="contact" style="left:28px"><span class="label">Website</span>www.tovartunes.es</div>
    <div class="contact" style="left:257px"><span class="label">Mail</span>mateo@tovartunes.es</div>

    <div class="brand-mark"><span class="dot"></span>TovarTunes</div>
  </main>
</body>
</html>
```